Design a (20.4 x 10.14) Banner that says - Keep Hope Rising From Harvest Glow TV Family

We want a design (20.4 x 10.14) with the words 'Keep Hope Rising' as the main text and 'From Harvest Glow TV Family' underneath. For 'Harvest Glow TV', we'd like you to use the logo which can be found in the image attached.

The image attached is just an example but please let your creative juices flow!

Target Market(s)

Christian

Industry/Entity Type

Christian

Requirements
Must have
• Must have the words 'Keep Hope Rising' and 'From Harvest Glow TV Family'.

```html
<!DOCTYPE html>
<html lang="en">
<head>
<meta charset="UTF-8">
<title>Keep Hope Rising – Harvest Glow TV Banner</title>
<link rel="stylesheet" href="https://fonts.googleapis.com/css2?family=Great+Vibes&family=Montserrat:ital,wght@0,400;0,600;1,400;1,500;1,800&display=swap">
<style>
  :root {
    --sun-glow: #fff4dc;
    --warm-sand: #e9c79a;
    --amber: #d08a45;
    --dusk-brown: #7a5236;
    --plum: #3a1a5c;
    --maroon: #7a2e45;
    --orange: #f27b0c;
    --white: #ffffff;
    --footer-ink: #4a3a30;
    --logo-ink: #2b2f7a;
  }
  * { margin: 0; padding: 0; box-sizing: border-box; }
  html, body { width: 1200px; height: 597px; overflow: hidden; background: var(--white); }
  .banner {
    position: relative;
    width: 1200px;
    height: 597px;
    overflow: hidden;
    font-family: "Montserrat", Arial, sans-serif;
  }
  .banner__photo {
    position: absolute;
    inset: 0;
    background:
      radial-gradient(circle at 78% 12%, var(--sun-glow) 0%, rgba(255,244,220,0.85) 14%, rgba(255,244,220,0) 42%),
      linear-gradient(90deg, var(--warm-sand) 0%, var(--amber) 26%, var(--dusk-brown) 52%, var(--warm-sand) 70%, #d9b58c 100%);
  }
  .banner__light {
    position: absolute;
    inset: 0;
    width: 100%;
    height: 100%;
  }
  .headline {
    position: absolute;
    inset: 0;
    font-weight: 400;
  }
  .headline__lead-in {
    position: absolute;
    left: 236px;
    top: 112px;
    font-style: italic;
    font-weight: 400;
    font-size: 40px;
    line-height: 1;
    color: var(--white);
    white-space: nowrap;
  }
  .headline__script {
    position: absolute;
    left: 0;
    top: 0;
    width: 1200px;
    height: 597px;
    overflow: visible;
  }
  .headline__script text {
    font-family: "Great Vibes", cursive;
    font-size: 240px;
    fill: url(#script-fill);
    stroke: rgba(255,255,255,0.8);
    stroke-width: 3px;
    paint-order: stroke fill;
  }
  .headline__close {
    position: absolute;
    left: 304px;
    top: 404px;
    font-style: italic;
    font-weight: 800;
    font-size: 76px;
    line-height: 1;
    letter-spacing: 1px;
    color: var(--maroon);
    white-space: nowrap;
  }
  .sign-off {
    position: absolute;
    left: 308px;
    top: 494px;
    font-style: italic;
    font-weight: 500;
    font-size: 20px;
    line-height: 1;
    color: var(--white);
    letter-spacing: 0.5px;
    white-space: nowrap;
  }
  .contact {
    position: absolute;
    left: 48px;
    top: 553px;
    display: flex;
    align-items: center;
    gap: 10px;
    font-size: 14px;
    font-weight: 600;
    color: var(--footer-ink);
    letter-spacing: 0.5px;
  }
  .contact__divider { font-weight: 400; }
  .contact__mark {
    width: 13px;
    height: 13px;
    background: var(--footer-ink);
  }
  .brand-tag {
    position: absolute;
    left: 912px;
    top: 510px;
    width: 234px;
    height: 54px;
    background: var(--white);
    display: flex;
    align-items: center;
    justify-content: center;
    font-weight: 600;
    font-size: 23px;
    color: var(--logo-ink);
    white-space: nowrap;
  }
</style>
</head>
<body>
  <main class="banner">
    <div class="banner__photo" role="img" aria-label="Sunlit photograph of a couple holding hands outdoors at sunset, a man in a plaid shirt and a woman in a floral skirt"></div>

    <svg class="banner__light" viewBox="0 0 1200 597" aria-hidden="true">
      <polygon points="0,597 0,520 620,0 1200,0 700,597" fill="rgba(255,255,255,0.14)"/>
      <polygon points="330,597 1200,170 1200,597" fill="rgba(255,255,255,0.12)"/>
    </svg>

    <h1 class="headline">
      <span class="headline__lead-in">Keep</span>
      <svg class="headline__script" viewBox="0 0 1200 597">
        <defs>
          <linearGradient id="script-fill" gradientUnits="userSpaceOnUse" x1="0" y1="170" x2="0" y2="410">
            <stop offset="0" stop-color="#3a1a5c"/>
            <stop offset="0.5" stop-color="#7a2e45"/>
            <stop offset="1" stop-color="#f27b0c"/>
          </linearGradient>
        </defs>
        <text x="40" y="350">Hope</text>
      </svg>
      <span class="headline__close">RISING</span>
    </h1>

    <p class="sign-off">From Harvest Glow TV Family</p>

    <footer class="contact">
      <span>www.harvestglow.tv</span>
      <span class="contact__divider">|</span>
      <span class="contact__mark"></span>
      <span>harvestglowmin</span>
    </footer>

    <div class="brand-tag">Harvest Glow TV</div>
  </main>
</body>
</html>
```